Harbinger Crude Advisors needs a logo design and business card layout.

HCA is a consulting firm in oil and gas, specializing in upstream engineering and field work. We provide engineering solutions for the complete wellbore cycle from casing design to flowback. This includes completion and production design. On-site job supervision and project engineering for conventional and unconventional reservoirs. Asset analysis by reviewing operational conditions of asset packages to determine value of potential acquisitions or divesture.

```html
<!DOCTYPE html>
<html lang="en">
<head>
<meta charset="utf-8">
<title>Harbinger Crude Advisors – Business Card</title>
<link rel="stylesheet" href="https://fonts.googleapis.com/css2?family=Open+Sans:wght@400;600;700&display=swap">
<style>
  :root {
    --stage: #8f8f8f;
    --card-white: #ffffff;
    --card-dark: #4a4a4a;
    --brand-red: #d6261c;
    --brand-orange: #f7941d;
    --ink: #444444;
    --ink-soft: #555555;
    --rule: #cfcfcf;
    --mark-dark: #3d3d3d;
  }
  * { margin: 0; padding: 0; box-sizing: border-box; }
  html, body { width: 1200px; height: 802px; overflow: hidden; }
  body {
    background: var(--stage);
    font-family: "Open Sans", Arial, sans-serif;
    position: relative;
  }
  .card {
    position: absolute;
    top: 274px;
    width: 443px;
    height: 265px;
    box-shadow: 2px 3px 5px rgba(0,0,0,0.35);
  }
  .card--front { left: 136px; background: var(--card-white); }
  .card--back  { left: 624px; background: var(--card-dark); overflow: hidden; }

  .brand {
    position: absolute;
    left: 20px;
    width: 184px;
    top: 78px;
    text-align: center;
  }
  .brand__square {
    display: block;
    width: 40px;
    height: 40px;
    margin: 0 auto 12px;
    background: var(--mark-dark);
    border-radius: 6px;
  }
  .brand__name {
    color: var(--brand-red);
    font-weight: 600;
    font-size: 17px;
    line-height: 1.2;
    letter-spacing: 0.3px;
  }

  .divider {
    position: absolute;
    left: 222px;
    top: 60px;
    width: 1px;
    height: 145px;
    background: var(--rule);
  }

  .contact {
    position: absolute;
    left: 246px;
    top: 60px;
    color: var(--ink);
  }
  .contact__name {
    color: var(--brand-red);
    font-weight: 700;
    font-size: 15.5px;
    line-height: 1.15;
    letter-spacing: 0.2px;
  }
  .contact__title {
    font-size: 12.5px;
    color: var(--ink-soft);
    margin-bottom: 9px;
  }
  .contact__list { list-style: none; font-size: 12.5px; line-height: 16px; }
  .contact__list li { display: flex; align-items: center; gap: 4px; }
  .contact__list svg { width: 10px; height: 10px; fill: var(--brand-red); flex: none; }
  .contact__address {
    margin-top: 3px;
    font-size: 12.8px;
    line-height: 16px;
    letter-spacing: 0.3px;
  }

  .back-pattern {
    position: absolute;
    inset: 0;
    background: linear-gradient(180deg, #4d4d4d, #474747);
  }
  .back-mark {
    position: absolute;
    left: 50%;
    top: 50%;
    transform: translate(-50%, -50%);
    text-align: center;
    margin-left: 42px;
    margin-top: 5px;
  }
  .back-mark__square {
    display: block;
    width: 44px;
    height: 52px;
    margin: 0 auto 5px;
    background: var(--card-white);
    border-radius: 6px;
  }
  .back-mark__name {
    color: var(--card-white);
    font-weight: 600;
    font-size: 13px;
    letter-spacing: 1px;
  }
</style>
</head>
<body>

<section class="card card--front">
  <div class="brand">
    <span class="brand__square"></span>
    <div class="brand__name">Harbinger Crude Advisors</div>
  </div>

  <div class="divider"></div>

  <div class="contact">
    <div class="contact__name">DELMAR WHITCOMBE</div>
    <div class="contact__title">Managing Director</div>
    <ul class="contact__list">
      <li>
        <svg viewBox="0 0 10 10" aria-hidden="true"><path d="M1 3c0-1.5 2-2 4-2s4 .5 4 2v1H7V3H3v1H1z M2 5h6l1 4H1z"/></svg>
        044-987 650 214
      </li>
      <li>
        <svg viewBox="0 0 10 10" aria-hidden="true"><path d="M2.5 0h5v10h-5z M3.5 1v7h3V1z"/></svg>
        044-987 650 317
      </li>
      <li>
        <svg viewBox="0 0 10 10" aria-hidden="true"><path d="M0 2h10v6H0z M1 2.8v.4l4 2.6 4-2.6v-.4l-4 2.5z" fill-rule="evenodd"/></svg>
        info@hcadvisors.com
      </li>
      <li>
        <svg viewBox="0 0 10 10" aria-hidden="true"><circle cx="5" cy="5" r="4.6"/></svg>
        www.hcadvisors.com
      </li>
    </ul>
    <div class="contact__address">4820, Refinery Row<br>Calder County, 770412.</div>
  </div>
</section>

<section class="card card--back">
  <div class="back-pattern" role="img" aria-label="Repeating tonal brand pattern in dark grey"></div>
  <div class="back-mark">
    <span class="back-mark__square"></span>
    <div class="back-mark__name">HCA</div>
  </div>
</section>

</body>
</html>
```